Process Roadmap for Interior Design Firm

We are looking to ramp up the design appeal of our current process roadmap to be very visually interesting, while staying informative and descriptive about our process.

Target Market(s)

In-house Clients

Industry/Entity Type

Interior Design Firm focused on sustainable and holistic design.

Other font styles liked:
• raleway

Requirements
Must have
• 1.) it would be nice if the graphic provided a more clear indication of the “journey” from one step to the next, so that there was a clear sense of the progression (such that we are directing the viewer) 2.). We would want it to fit on an 8.5”x11” page (the page could be horizontal when we have the Calm Compass formatted out with the testimonials) (in addition to the testimonials, we may also want to have the detailed descriptions of each step of the process presented below the graphic, so that the graphic is cleaner) 3.) ideally the graphic is clear and simple enough to also be used on our Bi-Weekly Client Updates, which will be typed updates for clients re their project budgets, schedule and scope. The Calm Compass graphic (without all the testimonials) would be at the end of the update, and would fit on the page horizontally at the bottom, perhaps in a space which is 7.5”w x 4”h or so.
Should not have
• bold or bright colors. Natural neutrals are preferred, such as the ones featured on the provided graphic.

```html
<!DOCTYPE html>
<html lang="en">
<head>
<meta charset="utf-8">
<title>Our Calm Compass – Elm Hollow Design</title>
<link href="https://fonts.googleapis.com/css2?family=Raleway:wght@400;500;700&display=swap" rel="stylesheet">
<style>
  :root {
    --canvas: #f2f2f2;
    --paper: #ffffff;
    --sand: #f1e9d8;
    --gold: #b99a5c;
    --taupe: #c9b99a;
    --slate: #7a7a7a;
    --ink: #333333;
    --white: #ffffff;
  }
  * { margin: 0; padding: 0; box-sizing: border-box; }
  html, body { width: 1200px; height: 885px; overflow: hidden; background: var(--canvas); }
  body { font-family: "Raleway", sans-serif; color: var(--ink); }

  .sheet {
    position: absolute; left: 141px; top: 52px;
    width: 918px; height: 710px;
    background: var(--paper);
    overflow: hidden;
  }

  .brand-name {
    position: absolute; left: 0; right: 0; top: 84px;
    text-align: center;
    font-weight: 500; font-size: 16px; letter-spacing: 0.22em;
    color: var(--gold);
  }

  .process-title {
    position: absolute; left: 0; right: 0; top: 143px;
    text-align: center;
    font-weight: 400; font-size: 42px; line-height: 48px;
    color: var(--ink);
  }
  .process-title .accent { color: var(--gold); }

  .roadmap {
    position: absolute; left: 73px; top: 212px;
    width: 771px; height: 72px;
  }
  .roadmap .path { fill: none; stroke: var(--gold); stroke-width: 1; }
  .roadmap .arrowhead { fill: var(--gold); }
  .roadmap .hex { fill: var(--paper); stroke-width: 4; stroke-linejoin: round; }
  .roadmap .hex--taupe { stroke: var(--taupe); }
  .roadmap .hex--slate { stroke: var(--slate); }
  .roadmap .icon { fill: none; stroke: var(--ink); stroke-width: 1.2; stroke-linecap: round; stroke-linejoin: round; }

  .step {
    position: absolute; top: 297px; width: 112px;
    text-align: center;
  }
  .step-name {
    font-weight: 700; font-size: 14.5px; letter-spacing: 0.02em;
    color: var(--gold); text-transform: uppercase;
    margin-bottom: 8px;
  }
  .step-text {
    font-size: 9.6px; line-height: 11.3px; color: var(--ink);
    padding: 0 4px;
  }
  .step-text + .step-text { margin-top: 11px; }

  .testimonials {
    position: absolute; left: 0; top: 483px;
    width: 918px; height: 227px;
    background: var(--sand);
  }
  .testimonials-title {
    position: absolute; left: 0; right: 0; top: 26px;
    text-align: center;
    font-weight: 500; font-size: 25px; color: var(--ink);
  }
  .testimonial-frame {
    position: absolute; left: 0; top: 0; width: 918px; height: 227px;
  }
  .testimonial-frame .rule,
  .testimonial-frame .hex { fill: none; stroke: var(--white); stroke-width: 2.5; }
  .quote {
    position: absolute; top: 109px; width: 124px;
    font-size: 9.6px; line-height: 11.3px; color: var(--ink);
  }
</style>
</head>
<body>
<main class="sheet">
  <div class="brand-name">ELM HOLLOW DESIGN</div>

  <h1 class="process-title">Our <span class="accent">Calm Compass</span></h1>

  <svg class="roadmap" viewBox="185 228 665 62" aria-hidden="true">
    <g class="paths">
      <polyline class="path" points="191,282 263,282 301,236 364,236"/>
      <polygon class="arrowhead" points="368,236 361,232.5 361,239.5"/>
      <polyline class="path" points="287,282 359,282 397,236 460,236"/>
      <polygon class="arrowhead" points="464,236 457,232.5 457,239.5"/>
      <polyline class="path" points="383,282 455,282 493,236 556,236"/>
      <polygon class="arrowhead" points="560,236 553,232.5 553,239.5"/>
      <polyline class="path" points="479,282 551,282 589,236 652,236"/>
      <polygon class="arrowhead" points="656,236 649,232.5 649,239.5"/>
      <polyline class="path" points="575,282 647,282 685,236 748,236"/>
      <polygon class="arrowhead" points="752,236 745,232.5 745,239.5"/>
      <polyline class="path" points="671,282 743,282 781,236 844,236"/>
      <polygon class="arrowhead" points="848,236 841,232.5 841,239.5"/>
    </g>

    <polygon class="hex hex--taupe" points="190,259 200,242 258,242 268,259 258,276 200,276"/>
    <polygon class="hex hex--slate" points="286,259 296,242 354,242 364,259 354,276 296,276"/>
    <polygon class="hex hex--taupe" points="382,259 392,242 450,242 460,259 450,276 392,276"/>
    <polygon class="hex hex--slate" points="478,259 488,242 546,242 556,259 546,276 488,276"/>
    <polygon class="hex hex--taupe" points="574,259 584,242 642,242 652,259 642,276 584,276"/>
    <polygon class="hex hex--slate" points="670,259 680,242 738,242 748,259 738,276 680,276"/>
    <polygon class="hex hex--taupe" points="766,259 776,242 834,242 844,259 834,276 776,276"/>

    <g class="icon">
      <circle cx="229" cy="257" r="7"/>
      <circle cx="229" cy="257" r="3.5"/>
      <line x1="229" y1="260.5" x2="229" y2="267"/>

      <path d="M316 259 Q325 251 334 259 Q325 267 316 259 Z"/>
      <circle cx="325" cy="259" r="2.6"/>

      <rect x="413" y="254" width="14" height="10"/>
      <line x1="418" y1="258" x2="430" y2="250"/>
      <line x1="416" y1="261" x2="423" y2="261"/>

      <rect x="509" y="252" width="16" height="13"/>
      <line x1="511" y1="263" x2="522" y2="254"/>
      <line x1="514" y1="256" x2="519" y2="256"/>

      <circle cx="613" cy="259" r="7.5"/>
      <polyline points="613,254 613,259 617,261"/>

      <circle cx="705" cy="257" r="6"/>
      <circle cx="705" cy="257" r="2.4"/>
      <line x1="709" y1="262" x2="716" y2="265"/>
      <line x1="699" y1="263" x2="694" y2="266"/>

      <path d="M805 256 C801 252 797 256 800 259 L805 263 L810 259 C813 256 809 252 805 256 Z"/>
      <path d="M795 262 Q799 268 805 268 Q811 268 815 262"/>
    </g>
  </svg>

  <section class="step" style="left:68px">
    <h2 class="step-name">Listening</h2>
    <p class="step-text">Listening to our clients, their land, and their home.</p>
    <p class="step-text">Identifying their needs, challenges, wishes, and dreams.</p>
  </section>
  <section class="step" style="left:179px">
    <h2 class="step-name">Visioning</h2>
    <p class="step-text">Facilitating a guided visioning process to clarify the deepest intention, true purpose, and highest potential for their home and their future within it.</p>
  </section>
  <section class="step" style="left:291px">
    <h2 class="step-name">Planning</h2>
    <p class="step-text">Turning our client’s vision into a clearly defined scope, budget, and timeline.</p>
    <p class="step-text">Mapping out the steps for making their dream a reality.</p>
    <p class="step-text">Setting a meeting schedule from start to finish.</p>
  </section>
  <section class="step" style="left:402px">
    <h2 class="step-name">Designing</h2>
    <p class="step-text">Following the schedule through the design phases from initial design concepts, technical drawings and details, and the selection of all finishes, fixtures, and furnishings.</p>
  </section>
  <section class="step" style="left:513px">
    <h2 class="step-name">Managing</h2>
    <p class="step-text">Coordinating with clients, builders, architects, and vendors to ensure that the design is executed with excellence, and the construction and furnishings are on-time and on-budget.</p>
  </section>
  <section class="step" style="left:625px">
    <h2 class="step-name">Installing</h2>
    <p class="step-text">Overseeing the inspection, installation, and arrangement of all furnishings, lighting, artwork, and decorative items.</p>
    <p class="step-text">Taking care of every last detail.</p>
  </section>
  <section class="step" style="left:736px">
    <h2 class="step-name">Completing</h2>
    <p class="step-text">Fixing any issues or defects.</p>
    <p class="step-text">Follow up on all remaining items.</p>
    <p class="step-text">Completing the final finishing touches to our client’s full and total satisfaction.</p>
  </section>

  <section class="testimonials">
    <svg class="testimonial-frame" viewBox="122 462 791 195" aria-hidden="true">
      <line class="rule" x1="122" y1="578" x2="194" y2="578"/>
      <line class="rule" x1="838" y1="578" x2="913" y2="578"/>
      <polygon class="hex" points="194,578 222,524 326,524 354,578 326,632 222,632"/>
      <polygon class="hex" points="356,578 384,524 488,524 516,578 488,632 384,632"/>
      <polygon class="hex" points="517,578 545,524 649,524 677,578 649,632 545,632"/>
      <polygon class="hex" points="678,578 706,524 810,524 838,578 810,632 706,632"/>
    </svg>
    <h2 class="testimonials-title">Testimonials</h2>
    <p class="quote" style="left:118px">Lorem ipsum dolor sit amet, consectetuer adipiscing elit, sed diam nonummy nibh euismod tincidunt ut laoreet dolore magna aliquam erat</p>
    <p class="quote" style="left:305px">Lorem ipsum dolor sit amet, consectetuer adipiscing elit, sed diam nonummy nibh euismod tincidunt ut laoreet dolore magna aliquam erat</p>
    <p class="quote" style="left:492px">Lorem ipsum dolor sit amet, consectetuer adipiscing elit, sed diam nonummy nibh euismod tincidunt ut laoreet dolore magna aliquam erat</p>
    <p class="quote" style="left:679px">Lorem ipsum dolor sit amet, consectetuer adipiscing elit, sed diam nonummy nibh euismod tincidunt ut laoreet dolore magna aliquam erat</p>
  </section>
</main>
</body>
</html>
```